Veltrane Management

We need a web design for a new consulting company, with clients all over the world. The company provides management consulting to the travel industry.

Logo files are attached.

Website must look very corporate and be responsive in design.

Management Consulting

```html
<!DOCTYPE html>
<html lang="en">
<head>
<meta charset="utf-8">
<title>Veltrane Management</title>
<link href="https://fonts.googleapis.com/css2?family=Cinzel:wght@400&family=Open+Sans:ital,wght@0,400;0,600;0,700;1,400&family=Roboto+Condensed:wght@400;700&family=Roboto:wght@400;700&display=swap" rel="stylesheet">
<style>
:root{
  --navy:#0b1d3a;
  --blue:#1a6fc4;
  --blue-light:#3f95dc;
  --green:#5cb21f;
  --green-dark:#3f8f10;
  --ink:#222;
  --wordmark:#333;
  --text:#444;
  --muted:#888;
  --page:#e9e9e9;
  --panel:#fff;
  --soft:#f3f3f3;
  --footer:#1d1d1d;
  --footer-deep:#121212;
}
*{margin:0;padding:0;box-sizing:border-box}
html,body{width:800px;height:1200px;overflow:hidden}
body{position:relative;background:var(--page);font-family:"Open Sans",sans-serif;color:var(--text)}
.abs{position:absolute}
.topline{left:0;top:0;width:800px;height:4px;background:var(--navy)}
.header{left:0;top:4px;width:800px;height:66px;background:linear-gradient(#fff,#f0f0f0)}
.brand-mark{left:92px;top:17px;width:38px;height:38px;border-radius:50%;background:var(--blue)}
.brand-name{left:140px;top:21px;font-family:"Open Sans",sans-serif;font-weight:600;color:var(--wordmark);font-size:22px;line-height:30px}
.help-icon{left:603px;top:25px;width:24px;height:24px;border-radius:4px;background:#333}
.help-label{left:636px;top:25px;font-size:8px;color:var(--muted);font-weight:600;letter-spacing:.4px}
.help-phone{left:636px;top:34px;font-family:"Roboto",sans-serif;font-weight:700;font-size:13px;color:#333}
.nav{left:0;top:70px;width:800px;height:29px;background:linear-gradient(var(--blue-light),#0f5fb0)}
.nav a{position:absolute;top:0;height:29px;line-height:29px;font-family:"Cinzel",serif;color:#fff;font-size:11px;text-decoration:none;text-align:center;letter-spacing:.4px}
.nav .sep{position:absolute;top:0;width:1px;height:29px;background:rgba(255,255,255,.28)}
.nav .active{background:linear-gradient(#7cc63a,var(--green-dark))}
.search{left:577px;top:73px;width:133px;height:23px;background:#fff;border-radius:2px;font-size:8px;color:#aaa;line-height:23px;padding-left:8px}
.search-btn{left:686px;top:73px;width:24px;height:23px;background:#2a2a2a;border-radius:0 2px 2px 0}
.hero{left:0;top:99px;width:800px;height:256px;background:linear-gradient(90deg,#e2e2e2,#f0f0f0 45%,#e9e9e9)}
.hero-photo{left:380px;top:99px;width:420px;height:256px;background:linear-gradient(90deg,rgba(230,230,230,0),#d9d9d9 25%,#c9ccd1 60%,#bcbfc5)}
.hero-title{left:107px;top:159px;font-family:"Roboto Condensed",sans-serif;font-weight:400;font-size:22px;line-height:27px;color:var(--ink)}
.hero-text{left:107px;top:214px;width:300px;font-size:11.3px;line-height:17px;color:#333}
.btn-green{background:linear-gradient(#7fcb3c,var(--green-dark));color:#fff;font-weight:700;text-align:center;font-family:"Roboto",sans-serif}
.hero-btn{left:108px;top:277px;width:96px;height:23px;line-height:23px;border-radius:12px;font-size:11px;box-shadow:0 2px 3px rgba(0,0,0,.25)}
.slide-arrow{top:213px;width:26px;height:26px;border-radius:50%;background:rgba(120,120,120,.55);border:2px solid rgba(255,255,255,.7)}
.panel{left:88px;top:355px;width:626px;height:600px;background:var(--panel);box-shadow:0 0 4px rgba(0,0,0,.12)}
.card{top:374px;width:188px;height:176px;border:1px solid #d6d6d6;border-radius:6px;background:#fff;overflow:hidden;box-shadow:0 3px 4px rgba(0,0,0,.07)}
.card-head{height:32px;background:linear-gradient(#fff,#eee);border-bottom:1px solid #ddd;position:relative}
.card-dot{position:absolute;left:8px;top:4px;width:22px;height:22px;border-radius:50%;background:var(--blue)}
.card-title{position:absolute;left:37px;top:8px;font-family:"Roboto",sans-serif;font-weight:700;font-size:12px;color:#333}
.card-title span{color:var(--green)}
.card-corner{position:absolute;right:0;bottom:0;width:0;height:0;border-left:28px solid transparent;border-bottom:28px solid var(--blue)}
.card-plus{position:absolute;right:3px;bottom:2px;color:#fff;font-weight:700;font-size:13px;line-height:13px}
.card-text{position:absolute;left:8px;top:38px;width:174px;font-size:7.7px;line-height:12px;color:#444}
.news{position:absolute;left:8px;width:172px}
.news-date{position:absolute;left:0;top:0;width:20px;height:22px;background:#555;color:#fff;font-size:7px;font-weight:700;text-align:center;line-height:10px;padding-top:1px}
.news-date b{display:block;background:#333}
.news-title{position:absolute;left:30px;top:0;font-size:8px;font-weight:700;color:#222}
.news-text{position:absolute;left:30px;top:13px;width:144px;font-size:7.8px;line-height:11px;color:#444}
.field{position:absolute;left:7px;width:174px;border:1px solid #d4d4d4;border-radius:2px;background:linear-gradient(#f4f4f4,#fff);font-size:8px;color:#777;padding:5px 6px}
.services{left:88px;top:583px;width:626px;height:264px;background:var(--soft)}
.services-tab{left:327px;top:584px;width:140px;height:19px;background:linear-gradient(#fff,#e6e6e6);border-radius:0 0 10px 10px;border:1px solid #d8d8d8;border-top:none;text-align:center;font-family:"Roboto",sans-serif;font-weight:700;font-size:12.5px;line-height:18px;color:#333}
.services-tab span{color:var(--green)}
.svc-line{height:1px;background:#dedede}
.svc-icon{width:57px;height:49px;border-radius:5px;background:linear-gradient(#fff,#dcdcdc);border:1px solid #cfcfcf;border-top:2px solid var(--green)}
.svc-icon svg{display:block;margin:8px auto 0}
.svc-title{font-family:"Roboto",sans-serif;font-weight:700;font-size:12px;color:#222}
.svc-text{width:212px;font-size:8.2px;line-height:12px;color:#444}
.testimonial{left:88px;top:847px;width:626px;height:108px;background:#e7e7e7}
.avatar{left:106px;top:868px;width:56px;height:56px;border-radius:50%;background:linear-gradient(#d7dde6,#8796ab);border:3px solid #fff;box-shadow:0 0 2px rgba(0,0,0,.3)}
.quote-mark{font-family:Georgia,serif;font-size:26px;color:#bbb;line-height:20px}
.quote{left:190px;top:870px;width:502px;font-style:italic;font-size:8.6px;line-height:14.5px;color:#444}
.quote-rule{left:188px;top:919px;width:498px;height:1px;background:#ccc}
.quote-name{left:192px;top:926px;font-size:9px;font-weight:700;color:var(--blue)}
.dot{top:933px;width:6px;height:6px;border-radius:50%;background:#ccc}
.footer{left:0;top:955px;width:800px;height:215px;background:linear-gradient(#2a2a2a,var(--footer) 30%,#161616)}
.newsletter{left:95px;top:967px;width:611px;height:40px;background:var(--footer-deep);border-radius:3px}
.nl-title{left:108px;top:974px;font-size:17px;color:#fff}
.nl-sep{left:259px;top:973px;width:1px;height:28px;background:#333}
.nl-text{left:272px;top:975px;font-size:9px;line-height:13px;color:#ddd;width:150px}
.nl-input{left:427px;top:979px;width:188px;height:19px;background:#fff;border-radius:2px;font-size:8px;color:#777;padding:4px 6px}
.nl-btn{left:620px;top:979px;width:75px;height:19px;line-height:19px;font-size:10.5px;border-radius:2px}
.foot-head{font-family:"Roboto",sans-serif;font-weight:700;font-size:12px;color:#fff}
.foot-rule{height:1px;background:#383838}
.foot-link{font-size:8.6px;color:#ddd}
.foot-link::before{content:"›";color:#777;margin-right:8px}
.foot-col-sep{width:1px;background:#2e2e2e}
.foot-text{font-size:8.6px;line-height:12px;color:#ddd}
.foot-logo-mark{left:598px;top:1057px;width:44px;height:44px;border-radius:50%;background:#fff}
.foot-logo-name{left:533px;top:1112px;width:174px;text-align:center;font-family:"Open Sans",sans-serif;font-weight:600;color:#fff;font-size:17px;line-height:22px}
.bottom{left:0;top:1170px;width:800px;height:30px;background:#0f0f0f}
.copy{left:102px;top:1180px;font-size:7.6px;color:#ccc}
.copy b{color:#fff}
.follow{left:555px;top:1178px;font-size:9.5px;color:#ddd;letter-spacing:.5px}
.social{top:1175px;width:19px;height:19px;border-radius:50%;background:#f2f2f2}
</style>
</head>
<body>
<div class="abs topline"></div>
<header class="abs header"></header>
<div class="abs brand-mark"></div>
<div class="abs brand-name">Veltrane Management</div>
<div class="abs help-icon"><svg width="24" height="24" viewBox="0 0 24 24"><path d="M8 6c1 0 2 2 2 3s-1 1-1 2 2 3 3 3 1-1 2-1 3 1 3 2-1 2-2 2c-4 0-9-5-9-9 0-1 1-2 2-2z" fill="#fff"/></svg></div>
<div class="abs help-label">HAPPY TO HELP?</div>
<div class="abs help-phone">012-555-0147</div>

<nav class="abs nav">
  <a class="active" style="left:89px;width:67px">HOME</a>
  <a style="left:160px;width:79px">ABOUT</a>
  <span class="sep" style="left:239px"></span>
  <a style="left:240px;width:87px">SERVICES</a>
  <span class="sep" style="left:327px"></span>
  <a style="left:328px;width:99px">RESOURCES</a>
  <span class="sep" style="left:427px"></span>
  <a style="left:428px;width:90px">CONTACT</a>
</nav>
<div class="abs search">search...</div>
<div class="abs search-btn"><svg width="24" height="23" viewBox="0 0 24 23"><circle cx="11" cy="10" r="4" stroke="#fff" stroke-width="1.8" fill="none"/><path d="M14 13l4 4" stroke="#fff" stroke-width="2"/></svg></div>

<section class="abs hero"></section>
<div class="abs hero-photo" role="img" aria-label="Photo of a consultant presenting a chart to colleagues at a meeting table"></div>
<h1 class="abs hero-title">We Provides Management<br>Consulting to the Travel Industry</h1>
<p class="abs hero-text">Lorem diam nonummy nibh esmod tincidu uta oreet dolore magna quam eratlutpat nim ad minim veniam quis nostrud nim adminim veniam.</p>
<div class="abs btn-green hero-btn">LEARN MORE</div>
<div class="abs slide-arrow" style="left:53px"><svg width="22" height="22" viewBox="0 0 22 22"><path d="M13 6l-5 5 5 5" stroke="#fff" stroke-width="1.6" fill="none"/></svg></div>
<div class="abs slide-arrow" style="left:722px"><svg width="22" height="22" viewBox="0 0 22 22"><path d="M9 6l5 5-5 5" stroke="#fff" stroke-width="1.6" fill="none"/></svg></div>

<main class="abs panel"></main>

<article class="abs card" style="left:100px">
  <div class="card-head"><span class="card-dot"></span><span class="card-title">ABOUT <span>VELTRANE</span></span></div>
  <p class="card-text">Lorem diam nonummy nibh esmod tincidu uta oreet dolore magna quam eratlutpat.nim ad minim veniam, quis nostrud nim adminim veniam, quis nostrud tationau ulamcorper scipit lortis nisl utnim ad minima veniarwem, quis nostrud exercitu ulamco suscipit lobortis nisl utnim nim veniam, quis nostrud exerci scipit lortis nisl utnim ad minima veniarwem, nisl utnim nim veniam, quis nostrud exerci tation ulamcorper suscipit</p>
  <span class="card-corner"></span><span class="card-plus">+</span>
</article>

<article class="abs card" style="left:307px">
  <div class="card-head"><span class="card-dot"></span><span class="card-title">LATEST <span>NEWS</span></span></div>
  <div class="news" style="top:42px">
    <div class="news-date"><b>09</b>OCT</div>
    <div class="news-title">Lorem ipsum dolor sit amet</div>
    <div class="news-text">is nisl utnim ad minima venam, quis nostrud exercin ulamcocipit lobortis nisl utnim nim veniam,is nisl utnimi ad minima veniam, quis</div>
  </div>
  <div style="position:absolute;left:8px;top:104px;width:172px;height:1px;background:#ddd"></div>
  <div class="news" style="top:114px">
    <div class="news-date"><b>09</b>OCT</div>
    <div class="news-title">Lorem ipsum dolor sit amet</div>
    <div class="news-text">Lorem ipsum smet consectetur mini adipisic elitsed do eit eim adosi miie vnioremipsuma</div>
  </div>
  <span class="card-corner"></span><span class="card-plus">+</span>
</article>

<article class="abs card" style="left:514px">
  <div class="card-head"><span class="card-dot"></span><span class="card-title">QUICK <span>CONTACT</span></span></div>
  <div class="field" style="top:42px;height:22px">Name</div>
  <div class="field" style="top:68px;height:22px">Email</div>
  <div class="field" style="top:94px;height:53px">Message</div>
  <span class="card-corner"></span><span class="card-plus">+</span>
</article>

<section class="abs services"></section>
<div class="abs services-tab">OUR <span>SERVICES</span></div>

<div class="abs svc-line" style="left:100px;top:622px;width:290px"></div>
<div class="abs svc-icon" style="left:111px;top:623px"><svg width="36" height="30" viewBox="0 0 36 30"><rect x="3" y="18" width="5" height="10" fill="#1c3d6b"/><rect x="11" y="14" width="5" height="14" fill="#1c3d6b"/><rect x="19" y="10" width="5" height="18" fill="#1c3d6b"/><rect x="27" y="6" width="5" height="22" fill="#1c3d6b"/><path d="M3 14l12-7 6 3 10-8" stroke="#1a6fc4" stroke-width="2.5" fill="none"/></svg></div>
<div class="abs svc-title" style="left:178px;top:628px">Sales/ Marketing</div>
<p class="abs svc-text" style="left:178px;top:644px">Lorem ipsum dolor sit amet consectetur elitsed do eiusmod tempor incididunt ut labore et dolore magna aliqua ut enim ad minim vesniam.</p>

<div class="abs svc-line" style="left:416px;top:622px;width:290px"></div>
<div class="abs svc-icon" style="left:427px;top:623px"><svg width="36" height="30" viewBox="0 0 36 30"><circle cx="14" cy="8" r="6" fill="#1e1e1e"/><path d="M3 28c0-8 5-12 11-12s11 4 11 12z" fill="#1e1e1e"/><circle cx="27" cy="22" r="7" fill="#1a6fc4" stroke="#fff" stroke-width="1.5"/><path d="M27 18v4h3" stroke="#fff" stroke-width="1.4" fill="none"/></svg></div>
<div class="abs svc-title" style="left:494px;top:628px">Strategic Planning</div>
<p class="abs svc-text" style="left:494px;top:644px">Lorem ipsum dolor sit amet consectetur elitsed do eiusmod tempor incididunt ut labore et dolore magna aliqua ut enim ad minim vesniam.</p>

<div class="abs svc-line" style="left:100px;top:694px;width:290px"></div>
<div class="abs svc-icon" style="left:111px;top:695px"><svg width="36" height="30" viewBox="0 0 36 30"><circle cx="12" cy="5" r="4" fill="#1e1e1e"/><rect x="7" y="10" width="10" height="18" rx="2" fill="#1e1e1e"/><circle cx="23" cy="18" r="8" fill="#1a6fc4" stroke="#fff" stroke-width="1.5"/><text x="23" y="22" font-size="11" font-weight="700" text-anchor="middle" fill="#fff" font-family="Roboto,sans-serif">$</text></svg></div>
<div class="abs svc-title" style="left:178px;top:700px">Human Capital Management Solutions</div>
<p class="abs svc-text" style="left:178px;top:716px">Lorem ipsum dolor sit amet consectetsed do eiusmod tempor incididunt ut labore et dolore magna aliqua ut enim ad minim vesniam.</p>

<div class="abs svc-line" style="left:416px;top:694px;width:290px"></div>
<div class="abs svc-icon" style="left:427px;top:695px"><svg width="36" height="30" viewBox="0 0 36 30"><rect x="2" y="3" width="28" height="20" fill="none" stroke="#1e1e1e" stroke-width="2.5"/><path d="M6 17l6-7 5 5 8-8" stroke="#1e1e1e" stroke-width="2" fill="none"/><circle cx="24" cy="20" r="5" fill="#fff" stroke="#1a6fc4" stroke-width="2.2"/><path d="M28 24l5 5" stroke="#1a6fc4" stroke-width="3"/></svg></div>
<div class="abs svc-title" style="left:494px;top:700px">Financial Analysis</div>
<p class="abs svc-text" style="left:494px;top:716px">Lorem ipsum dolor sit amet consectetur elitsed do eiusmod tempor incididunt ut labore et dolore magna aliqua ut enim ad minim vesniam.</p>

<div class="abs svc-line" style="left:100px;top:773px;width:290px"></div>
<div class="abs svc-icon" style="left:111px;top:774px"><svg width="36" height="30" viewBox="0 0 36 30"><rect x="2" y="8" width="28" height="19" rx="2" fill="#1e1e1e"/><path d="M11 8V4h10v4" stroke="#1e1e1e" stroke-width="2.5" fill="none"/><rect x="14" y="14" width="4" height="4" fill="#fff"/><circle cx="29" cy="24" r="5" fill="#1a6fc4"/></svg></div>
<div class="abs svc-title" style="left:178px;top:779px">Cash Management Solutions</div>
<p class="abs svc-text" style="left:178px;top:795px">Lorem ipsum dolor sit amet consectetur elitsed do eiusmod tempor incididunt ut labore et dolore magna aliqua ut enim ad minim vesniam.</p>

<div class="abs svc-line" style="left:416px;top:773px;width:290px"></div>
<div class="abs svc-icon" style="left:427px;top:774px"><svg width="36" height="30" viewBox="0 0 36 30"><path d="M7 17v-3a11 11 0 0 1 22 0v3" stroke="#1e1e1e" stroke-width="2.5" fill="none"/><rect x="5" y="15" width="6" height="10" rx="2" fill="#1e1e1e"/><rect x="25" y="15" width="6" height="10" rx="2" fill="#1e1e1e"/><path d="M28 25c0 3-4 4-8 4" stroke="#1a6fc4" stroke-width="2" fill="none"/></svg></div>
<div class="abs svc-title" style="left:494px;top:779px">Customer Support</div>
<p class="abs svc-text" style="left:494px;top:795px">Lorem ipsum dolor sit amet consectetur elitsed do eiusmod tempor incididunt ut labore et dolore magna aliqua ut enim ad minim vesniam.</p>

<section class="abs testimonial"></section>
<div class="abs avatar" role="img" aria-label="Portrait photo of the client giving the testimonial"></div>
<div class="abs quote-mark" style="left:178px;top:866px">“</div>
<blockquote class="abs quote">Lorem ipsum dolor sit amet consectetur adipisicing elitsed do eiusmod tempor incididunt ut labore et dolore magna aliqua. Ut enim ad minim vesniam, quis nostrud exercitation ullamco laboris nisi ut aliquip ex ea commodo consequat. Duis aute irure dolor in reprehenderit in voluptate velit esse cillum is a dolore eu fugiat nulla pariatur. Excepteur sint occaecat cupidatat non proi</blockquote>
<div class="abs quote-mark" style="left:650px;top:903px">”</div>
<div class="abs quote-rule"></div>
<div class="abs quote-name">Daniel Marsh</div>
<span class="abs dot" style="left:648px;background:var(--green)"></span>
<span class="abs dot" style="left:657px"></span>
<span class="abs dot" style="left:666px"></span>
<span class="abs dot" style="left:675px"></span>

<footer class="abs footer"></footer>
<div class="abs newsletter"></div>
<div class="abs nl-title">Newsletter Signup</div>
<div class="abs nl-sep"></div>
<div class="abs nl-text">Get latest updates by entering your email address.</div>
<div class="abs nl-input">Enter your Email...</div>
<div class="abs btn-green nl-btn">SUBSCRIBE</div>

<div class="abs foot-head" style="left:101px;top:1041px">QUICK LINKS</div>
<div class="abs foot-rule" style="left:101px;top:1062px;width:186px"></div>
<div class="abs foot-link" style="left:105px;top:1071px">Home</div>
<div class="abs foot-rule" style="left:101px;top:1092px;width:82px"></div>
<div class="abs foot-link" style="left:105px;top:1100px">Services</div>
<div class="abs foot-rule" style="left:101px;top:1121px;width:82px"></div>
<div class="abs foot-link" style="left:105px;top:1130px">Contact Us</div>
<div class="abs foot-link" style="left:205px;top:1074px">About Us</div>
<div class="abs foot-rule" style="left:203px;top:1094px;width:84px"></div>
<div class="abs foot-link" style="left:205px;top:1100px">Resources</div>
<div class="abs foot-rule" style="left:203px;top:1121px;width:84px"></div>
<div class="abs foot-col-sep" style="left:300px;top:1035px;height:130px"></div>

<div class="abs foot-head" style="left:319px;top:1041px">CONTACT US</div>
<div class="abs foot-rule" style="left:319px;top:1062px;width:190px"></div>
<svg class="abs" style="left:319px;top:1075px" width="10" height="12" viewBox="0 0 10 12"><path d="M5 0a4 4 0 0 1 4 4c0 3-4 8-4 8S1 7 1 4a4 4 0 0 1 4-4z" fill="#eee"/><circle cx="5" cy="4" r="1.5" fill="#1d1d1d"/></svg>
<div class="abs foot-text" style="left:339px;top:1074px;width:172px">Lorem ipsum dolor sit amet consecttuer adi piscing elit diam non</div>
<svg class="abs" style="left:319px;top:1107px" width="10" height="10" viewBox="0 0 10 10"><path d="M2 0c1 0 2 2 2 3L3 4c1 1 2 2 3 3l1-1c1 0 3 1 3 2s-1 2-2 2C4 10 0 6 0 2 0 1 1 0 2 0z" fill="#eee"/></svg>
<div class="abs foot-text" style="left:339px;top:1106px">012-555-0147</div>
<svg class="abs" style="left:319px;top:1129px" width="10" height="8" viewBox="0 0 10 8"><rect width="10" height="8" fill="#eee"/><path d="M0 0l5 4 5-4" stroke="#1d1d1d" fill="none"/></svg>
<div class="abs foot-text" style="left:339px;top:1126px">info@veltranestrategy.com</div>
<div class="abs foot-col-sep" style="left:524px;top:1025px;height:145px"></div>

<div class="abs foot-logo-mark"></div>
<div class="abs foot-logo-name">Veltrane Management</div>

<div class="abs bottom"></div>
<div class="abs copy">Copyright 2014 <b>veltranestrategymanagement.</b> All Right Reserved.</div>
<div class="abs follow">FOLLOW US :</div>
<span class="abs social" style="left:618px;background:var(--green)"></span>
<span class="abs social" style="left:643px"></span>
<span class="abs social" style="left:667px"></span>
<span class="abs social" style="left:691px"></span>
</body>
</html>
```